Lustiges Einladungskarten-Design für Feier gesucht
Zielgruppe
private Einladung
Aufgabenstellung
Einladung im Posterformat DIN A2 dass auf DINA A6 (9 einzelne Felder) runter gefaltet werden kann.
Die Einladung soll lustig, witzig und ausgefallen sein - auf keinen Fall klassisch, schnörkelig, spießig.
Die Location soll genannt werden: eine bewirtete Waldhütte im Sauerland, Übernachtungsmöglichkeiten, Beginn der Feier: 18.30 Uhr am 29.09.2018
Es handelt sich um eine Feier zum 50.Geburtstag, zum 46. Geburtstag, zur Hochzeit – aber vor allem feiern wir die das Leben, die Liebe und unsere Freunde.
Es ist eine Grillparty – kein Dresscode, keine Spiele – sondern essen, trinken, feiern, tanzen, Spaß haben.
Gern handlettering , illustriert oder andere kreative Ideen.

```html
<!DOCTYPE html>
<html lang="de">
<head>
<meta charset="utf-8">
<title>Einladung – Bist du Wald?</title>
<link rel="stylesheet" href="https://fonts.googleapis.com/css2?family=Amatic+SC:wght@400;700&display=swap">
<style>
  :root {
    --frame: #e2e3dd;
    --paper: #ffffff;
    --panel: #e2e3dd;
    --ink: #3f3532;
    --green: #a8c83a;
    --hand: "Amatic SC", cursive;
  }
  * { box-sizing: border-box; margin: 0; padding: 0; }
  html, body { width: 849px; height: 1200px; overflow: hidden; background: var(--frame); }
  .poster {
    position: absolute; left: 12px; top: 17px; width: 825px; height: 1166px;
    background: var(--paper);
  }
  .fold-grid {
    position: absolute; left: 41px; top: 58px; width: 742px; height: 1050px;
    display: grid; grid-template-columns: repeat(3, 1fr); grid-template-rows: repeat(3, 1fr);
    background: var(--panel);
  }
  .panel { position: relative; overflow: hidden; font-family: var(--hand); color: var(--ink); font-weight: 700; }
  .line { position: absolute; line-height: 1; white-space: nowrap; }
  .center { left: 0; width: 100%; text-align: center; }
  .accent { color: var(--green); }
  .art { position: absolute; border-radius: 10px; }
  .art.green { background: var(--green); }
  .art.mixed { background: linear-gradient(135deg, var(--green), #7c8a3c 60%, var(--ink)); }
  .art.dark { background: linear-gradient(180deg, #5a4d47, var(--ink)); }
  .vertical { position: absolute; line-height: 1; white-space: nowrap; transform: translate(-50%, -50%) rotate(-90deg); }
  .small { font-size: 17px; }
</style>
</head>
<body>
<main class="poster">
  <section class="fold-grid">

    <!-- 1 -->
    <article class="panel panel-question">
      <p class="line center" style="top:22px;font-size:118px;">Bist</p>
      <div class="art green" style="left:18px;top:150px;width:40px;height:80px;" role="img" aria-label="Gezeichnete Tanne"></div>
      <p class="line center" style="top:138px;font-size:96px;">d<span class="accent">u</span></p>
      <div class="art green" style="left:175px;top:145px;width:55px;height:80px;" role="img" aria-label="Gezeichneter Laubbaum"></div>
      <p class="line center" style="top:228px;font-size:100px;">Wald?</p>
    </article>

    <!-- 2 -->
    <article class="panel panel-dresscode">
      <p class="line center" style="top:38px;font-size:54px;">dann zieh an</p>
      <p class="line center" style="top:100px;font-size:46px;">was du willst!</p>
      <div class="art mixed" style="left:19px;top:155px;width:106px;height:87px;" role="img" aria-label="Gezeichnetes T-Shirt"></div>
      <div class="art green" style="left:150px;top:148px;width:46px;height:40px;" role="img" aria-label="Gezeichnete Krone"></div>
      <div class="art mixed" style="left:135px;top:196px;width:82px;height:48px;" role="img" aria-label="Gezeichnete Fliege"></div>
      <p class="line center" style="top:252px;font-size:70px;">oder nix</p>
    </article>

    <!-- 3 -->
    <article class="panel panel-location">
      <p class="line" style="left:18px;top:38px;font-size:46px;">egal wie</p>
      <div class="art green" style="left:168px;top:44px;width:31px;height:31px;border-radius:50%;" role="img" aria-label="Gezeichneter Kompass"></div>
      <p class="line center" style="top:78px;font-size:50px;">aber komm zur</p>
      <div class="art green" style="left:21px;top:142px;width:56px;height:52px;" role="img" aria-label="Gezeichnetes Flugzeug"></div>
      <div class="art green" style="left:84px;top:150px;width:64px;height:40px;" role="img" aria-label="Gezeichnetes Auto"></div>
      <div class="art mixed" style="left:155px;top:142px;width:65px;height:46px;" role="img" aria-label="Gezeichnetes Fahrrad"></div>
      <p class="line center" style="top:212px;font-size:52px;">waldhütte im</p>
      <p class="line center" style="top:254px;font-size:66px;">Sauerland</p>
    </article>

    <!-- 4 -->
    <article class="panel panel-date">
      <p class="line center" style="top:38px;font-size:60px;">am Besten</p>
      <p class="line center" style="top:96px;font-size:48px;">am 29.9.2018</p>
      <div class="art green" style="left:83px;top:163px;width:75px;height:94px;" role="img" aria-label="Gezeichneter Kalender mit 29. Sept 2018"></div>
      <div class="art green" style="left:15px;top:292px;width:14px;height:26px;" role="img" aria-label="Gezeichnete Glühbirne"></div>
      <p class="line small" style="left:42px;top:296px;">denn da sind auch die anderen da</p>
    </article>

    <!-- 5 -->
    <article class="panel panel-time">
      <div class="art green" style="left:91px;top:35px;width:68px;height:63px;" role="img" aria-label="Gezeichneter Vogel"></div>
      <p class="vertical" style="left:121px;top:212px;font-size:100px;">18.30</p>
    </article>

    <!-- 6 -->
    <article class="panel panel-reasons">
      <div class="art green" style="left:32px;top:25px;width:39px;height:60px;" role="img" aria-label="Gezeichneter Keimling"></div>
      <p class="line" style="left:84px;top:26px;font-size:66px;">leben</p>
      <div class="art dark" style="left:20px;top:103px;width:28px;height:46px;" role="img" aria-label="Zwei gezeichnete Figuren"></div>
      <p class="line" style="left:62px;top:90px;font-size:70px;">freunde</p>
      <svg class="heart" style="position:absolute;left:32px;top:170px;" width="46" height="46" viewBox="0 0 46 46" aria-hidden="true">
        <path d="M23 42 C8 30 2 22 2 13 C2 6 8 2 13 2 C18 2 21 5 23 9 C25 5 28 2 33 2 C38 2 44 6 44 13 C44 22 38 30 23 42 Z" fill="var(--green)" stroke="var(--ink)" stroke-width="2"/>
      </svg>
      <p class="line" style="left:92px;top:160px;font-size:66px;">liebe</p>
      <p class="line center" style="top:250px;font-size:22px;">wenn dir noch ein weiterer</p>
      <p class="line center" style="top:270px;font-size:22px;">grund zum feiern einfällt</p>
      <p class="line center" style="top:290px;font-size:32px;">Bring ihn mit!!</p>
    </article>

    <!-- 7 -->
    <article class="panel panel-stay">
      <p class="line center" style="top:30px;font-size:20px;">du findest dein auto nicht mehr?</p>
      <p class="line center" style="top:52px;font-size:20px;">oder hast plötzlich 2 davon?</p>
      <div class="art green" style="left:51px;top:92px;width:62px;height:38px;" role="img" aria-label="Gezeichnetes Auto"></div>
      <div class="art green" style="left:127px;top:92px;width:62px;height:38px;" role="img" aria-label="Gezeichnetes Auto"></div>
      <p class="line center" style="top:146px;font-size:46px;">dann übernachte</p>
      <p class="line center" style="top:188px;font-size:46px;">besser hier!</p>
      <div class="art mixed" style="left:56px;top:250px;width:64px;height:58px;" role="img" aria-label="Gezeichnete Reisetasche"></div>
      <div class="art green" style="left:134px;top:242px;width:53px;height:68px;" role="img" aria-label="Gezeichnetes Haus"></div>
    </article>

    <!-- 8 -->
    <article class="panel panel-fun">
      <div class="art green" style="left:44px;top:43px;width:60px;height:87px;" role="img" aria-label="Gezeichnete Hand, die nach unten zeigt"></div>
      <p class="line" style="left:35px;top:150px;font-size:50px;">essen</p>
      <p class="line" style="left:35px;top:208px;font-size:50px;">feiern</p>
      <p class="line" style="left:35px;top:268px;font-size:50px;">trinken</p>
      <p class="vertical" style="left:186px;top:175px;font-size:72px;">spass haben</p>
    </article>

    <!-- 9 -->
    <article class="panel panel-goodbye">
      <div class="art dark" style="left:97px;top:104px;width:53px;height:83px;" role="img" aria-label="Gezeichnetes Fernglas mit kleinem Vogel"></div>
      <p class="line center" style="top:200px;font-size:56px;">see you</p>
    </article>

  </section>
</main>
</body>
</html>
```